Trade Show Booth Design for Saas company

Brightpost Suite is a startup company that will be launching its software as a service product at a trade show in the near future. We are looking for something that really pops and is appealing to the eye. Attached is the branding guidelines along with the color palette. The pink should be predominant. We’re not so concerned with the copy of your design for the contest, but rather the design itself. We can work on the copy later. You can utilize any copy or graphics from our website at www.brightpostsuite.example. You can also learn more about us at the website. One element from the website that is worth mentioning, and optional, is the hub and spoke graphic in the “Connect All Your SMTP Email Service Providers” section. (It is attached.) We will provide high resolution versions of anything you need. The display will be a flat 10 foot wide by 8 foot tall, one piece of fabric. We will also need the graphics for the 39in x 19in x 12in Counter Graphic Print, but probably just the logo on it. We are open to design elements that include the use of a person or not. We basically want something modern and very eye-catching.
Potential headline and text:
One place to manage it all
Guided by expert mailers, Brightpost Suite combines every aspect of email marketing into a powerful package.

```html
<!DOCTYPE html>
<html lang="en">
<head>
<meta charset="utf-8">
<title>Brightpost Suite – Trade Show Backdrop and Counter Graphic</title>
<link rel="stylesheet" href="https://fonts.googleapis.com/css2?family=Montserrat:wght@400;500;600;700;800&display=swap">
<style>
  :root {
    --pink: #ec0c7c;
    --pink-deep: #e40a74;
    --navy: #17163f;
    --yellow: #eef019;
    --white: #ffffff;
    --panel: #f4f4f6;
    --stage: #e3e3e5;
    --grey-text: #55566a;
    --cyan: #2fb8ec;
  }
  * { box-sizing: border-box; margin: 0; padding: 0; }
  html, body { width: 1200px; height: 2281px; overflow: hidden; }
  body {
    background: var(--stage);
    font-family: "Montserrat", Arial, sans-serif;
    color: var(--navy);
    position: relative;
  }

  /* Backdrop panel */
  .backdrop {
    position: absolute; left: 100px; top: 180px;
    width: 1000px; height: 1000px;
    background: linear-gradient(135deg, #ffffff 0%, var(--panel) 55%, #ececef 100%);
    box-shadow: 14px 18px 28px rgba(0,0,0,.28);
    overflow: hidden;
  }
  .backdrop .navy-band {
    position: absolute; left: 0; right: 0; top: 705px; bottom: 0;
    background: var(--navy);
  }
  .brand {
    position: absolute; left: 0; right: 0; top: 110px;
    display: flex; justify-content: center; align-items: center; gap: 18px;
  }
  .brand-square { width: 46px; height: 46px; background: var(--pink); }
  .brand-name {
    font-weight: 700; font-size: 46px; color: var(--navy); letter-spacing: 0.5px;
  }

  .bracket { position: absolute; width: 72px; height: 72px; }
  .bracket-tl { left: 175px; top: 262px; border-left: 16px solid var(--pink); border-top: 16px solid var(--pink); }
  .bracket-br { left: 778px; top: 406px; border-right: 16px solid var(--pink); border-bottom: 16px solid var(--pink); }

  .headline {
    position: absolute; left: 0; right: 0; top: 290px; text-align: center;
    color: var(--navy); text-transform: uppercase; line-height: 1.2;
  }
  .headline .line-one { display: block; font-size: 42px; font-weight: 500; padding-left: 40px; }
  .headline .line-two { display: block; font-size: 46px; font-weight: 800; }
  .headline .accent { color: var(--pink); font-weight: 800; }

  .intro {
    position: absolute; left: 0; right: 0; top: 422px; text-align: center;
    font-size: 18px; line-height: 1.5; color: var(--grey-text);
  }

  .service-grid {
    position: absolute; left: 91px; top: 509px; width: 818px; height: 364px;
    display: grid; grid-template-columns: repeat(3, 1fr); grid-template-rows: repeat(2, 1fr);
    gap: 3px;
  }
  .service {
    background: var(--pink);
    display: flex; flex-direction: column; align-items: center; justify-content: center;
    color: var(--white); font-weight: 700; font-size: 19px; text-align: center; line-height: 1.3;
  }
  .service.highlight { background: var(--yellow); color: var(--navy); }
  .service-icon {
    width: 44px; height: 44px; margin-bottom: 14px;
    background: var(--white); border-radius: 5px;
    display: flex; align-items: center; justify-content: center;
  }
  .service.highlight .service-icon { background: var(--pink); }

  .contact-bar {
    position: absolute; left: 0; right: 0; top: 918px;
    display: flex; justify-content: center; align-items: center; gap: 10px;
    color: var(--white); font-size: 20px; font-weight: 500;
  }
  .contact-bar .accent { color: var(--cyan); font-weight: 700; }
  .contact-bar .divider { opacity: .8; }
  .contact-item { display: flex; align-items: center; gap: 6px; }

  /* Counter graphic */
  .counter {
    position: absolute; left: 100px; top: 1320px;
    width: 1000px; height: 485px;
    background: var(--pink-deep);
    box-shadow: 14px 18px 28px rgba(0,0,0,.28);
  }
  .counter-plate {
    position: absolute; left: 323px; top: 107px; width: 354px; height: 281px;
    background: var(--white);
  }
  .counter-plate .inner-frame {
    position: absolute; inset: 14px; border: 3px solid var(--navy);
  }
  .counter-plate .brand-name {
    position: absolute; left: 0; right: 0; top: 104px; text-align: center; font-size: 34px;
  }
  .counter-plate .plate-url {
    position: absolute; left: 0; right: 0; bottom: 8px; text-align: center;
  }
  .counter-plate .plate-url span {
    background: var(--white); padding: 0 8px; font-size: 15px; font-weight: 500; color: var(--navy);
  }
  .counter-plate .plate-url .accent { color: var(--pink); font-weight: 700; padding: 0; }
  .plate-corner { position: absolute; width: 30px; height: 30px; }
  .plate-corner-tl { left: -22px; top: -22px; border-left: 8px solid var(--white); border-top: 8px solid var(--white); }
  .plate-corner-br { right: -22px; bottom: -22px; border-right: 8px solid var(--white); border-bottom: 8px solid var(--white); }
</style>
</head>
<body>

<section class="backdrop" aria-label="Backdrop panel">
  <div class="navy-band"></div>

  <div class="brand">
    <span class="brand-square"></span>
    <span class="brand-name">Brightpost Suite</span>
  </div>

  <span class="bracket bracket-tl"></span>
  <span class="bracket bracket-br"></span>

  <h1 class="headline">
    <span class="line-one">Work with <span class="accent">mailers</span></span>
    <span class="line-two">Who know how to <span class="accent">mail</span></span>
  </h1>

  <p class="intro">Guided by expert mailers, Brightpost Suite combines every aspect<br>of email marketing into a powerful package.</p>

  <div class="service-grid">
    <div class="service">
      <span class="service-icon"><svg width="26" height="26" viewBox="0 0 26 26" fill="none" stroke="#ec0c7c" stroke-width="2"><path d="M5 21 L11 15 M9 9 L20 5 L17 16 L11 19 L7 15 Z"/></svg></span>
      In-house<br>SMTP
    </div>
    <div class="service">
      <span class="service-icon"><svg width="26" height="26" viewBox="0 0 26 26" fill="none" stroke="#ec0c7c" stroke-width="2"><path d="M6 15 a5 5 0 0 1 3-9 a6 6 0 0 1 11 3 a4 4 0 0 1 0 6 Z M9 18v3 M13 18v4 M17 18v3"/></svg></span>
      Email<br>Automation
    </div>
    <div class="service">
      <span class="service-icon"><svg width="26" height="26" viewBox="0 0 26 26" fill="none" stroke="#ec0c7c" stroke-width="2"><rect x="4" y="8" width="18" height="13"/><path d="M4 8 L13 15 L22 8"/><circle cx="13" cy="7" r="3"/></svg></span>
      Email<br>Validation
    </div>
    <div class="service">
      <span class="service-icon"><svg width="26" height="26" viewBox="0 0 26 26" fill="none" stroke="#ec0c7c" stroke-width="2"><rect x="7" y="8" width="12" height="10" rx="2"/><path d="M3 11h4 M3 15h4 M19 11h4 M19 15h4 M11 4v4 M15 4v4 M11 18v4 M15 18v4"/></svg></span>
      API<br>Connections
    </div>
    <div class="service highlight">
      <span class="service-icon"><svg width="26" height="26" viewBox="0 0 26 26" fill="none" stroke="#ffffff" stroke-width="2"><rect x="4" y="5" width="18" height="16" rx="2"/><path d="M4 9h18 M11 13l-2 2 2 2 M15 13l2 2-2 2"/></svg></span>
      Multiple SMTP<br>Connections
    </div>
    <div class="service">
      <span class="service-icon"><svg width="26" height="26" viewBox="0 0 26 26" fill="none" stroke="#ec0c7c" stroke-width="2"><rect x="4" y="4" width="18" height="18"/><path d="M8 18v-4 M12 18v-8 M16 18v-6 M20 18v-10"/></svg></span>
      Reporting<br>and Analytics
    </div>
  </div>

  <div class="contact-bar">
    <span class="contact-item"><svg width="20" height="20" viewBox="0 0 20 20" fill="none" stroke="#2fb8ec" stroke-width="1.8"><circle cx="10" cy="10" r="8"/><path d="M2 10h16 M10 2c3 3 3 13 0 16 M10 2c-3 3-3 13 0 16"/></svg>www.<span class="accent">brightpostsuite</span>.example</span>
    <span class="divider">|</span>
    <span class="contact-item"><svg width="20" height="20" viewBox="0 0 20 20" fill="none" stroke="#2fb8ec" stroke-width="1.8"><circle cx="10" cy="10" r="8"/><rect x="5.5" y="7" width="9" height="6"/><path d="M5.5 7l4.5 3.5L14.5 7"/></svg>info@<span class="accent">brightpostsuite</span>.example</span>
    <span class="divider">|</span>
    <span class="contact-item accent"><svg width="20" height="20" viewBox="0 0 20 20" fill="none" stroke="#2fb8ec" stroke-width="1.8"><circle cx="10" cy="10" r="8"/><path d="M7 6l2 2-1 1.5c.7 1.3 1.8 2.4 3 3L12.5 11.5l2 2-1.5 1.5C9.5 14.5 5.5 10.5 5.5 7.5Z"/></svg>+1 (555) 010-0199</span>
  </div>
</section>

<section class="counter" aria-label="Counter graphic">
  <div class="counter-plate">
    <span class="plate-corner plate-corner-tl"></span>
    <span class="plate-corner plate-corner-br"></span>
    <div class="inner-frame"></div>
    <div class="brand-name">Brightpost Suite</div>
    <div class="plate-url"><span>www.<span class="accent">brightpostsuite</span>.example</span></div>
  </div>
</section>

</body>
</html>
```